Need Business Card ASAP

We need a business card design for a meeting coming up in a few days. The company name is Halvorne Building and Construction and the logo is attached. Something clean, cool, and contemporary that we can get to a printer right away. Attached is the business card for Murrow Energy, an affiliated company, which we like. Instead of the hawk on the back, you could use the attached "D". We'll also be needing matching letterhead in the near future, so ideas for that are welcome.

```html
<!DOCTYPE html>
<html lang="en">
<head>
<meta charset="utf-8">
<title>Halvorne Building and Construction – Business Card</title>
<link href="https://fonts.googleapis.com/css2?family=Exo+2:wght@400;500&family=Oswald:wght@400;500&display=swap" rel="stylesheet">
<style>
  :root {
    --backdrop: #e3e3e1;
    --card: #ffffff;
    --gold: #b9ae78;
    --gold-light: #d8d1a8;
    --ink: #231f20;
    --ink-soft: #3a3536;
  }
  * { box-sizing: border-box; margin: 0; padding: 0; }
  html, body { width: 1200px; height: 933px; overflow: hidden; }
  body {
    background: var(--backdrop);
    font-family: "Exo 2", sans-serif;
    color: var(--ink);
    position: relative;
  }
  .card {
    position: absolute;
    left: 290px;
    width: 620px;
    height: 354px;
    background: var(--card);
    box-shadow: 0 6px 18px rgba(0,0,0,0.18);
    overflow: hidden;
  }
  .card--back { top: 62px; }
  .card--front { top: 517px; }

  /* Brand block */
  .brand {
    position: absolute;
    width: 118px;
    display: flex;
    flex-direction: column;
    align-items: flex-start;
    gap: 8px;
  }
  .brand__mark {
    width: 34px; height: 34px;
    background: var(--gold);
  }
  .brand__name {
    font-family: "Exo 2", sans-serif;
    font-weight: 500;
    font-size: 14px;
    line-height: 1.2;
    color: var(--ink);
  }
  .card--back .brand { left: 470px; top: 150px; }
  .card--front .brand { left: 470px; top: 90px; }

  /* Back */
  .back__panel {
    position: absolute;
    left: 95px; top: 0;
    width: 160px; height: 150px;
    background: radial-gradient(circle at 60% 50%, var(--gold-light) 0%, var(--gold) 55%);
  }

  /* Front */
  .contact-panel {
    position: absolute;
    left: 70px; top: 70px;
    width: 175px; height: 195px;
    background: radial-gradient(circle at 70% 40%, var(--gold-light) 0%, var(--gold) 70%);
    padding: 16px 14px;
    font-size: 11.5px;
    line-height: 1.35;
    color: var(--ink-soft);
  }
  .contact-panel__address { margin-bottom: 16px; }
  .contact-list { list-style: none; }
  .contact-list li {
    display: flex; align-items: center; gap: 7px;
    margin-bottom: 4px;
    font-size: 10.5px;
  }
  .contact-list svg { width: 10px; height: 10px; flex: none; fill: var(--ink-soft); }

  .divider {
    position: absolute;
    left: 245px; right: 0; top: 196px;
    height: 4px;
    background: var(--ink);
  }
  .person {
    position: absolute;
    left: 258px; top: 208px;
  }
  .person__name {
    font-family: "Oswald", sans-serif;
    font-weight: 400;
    font-size: 27px;
    letter-spacing: 0.5px;
    line-height: 1.1;
    color: var(--ink);
  }
  .person__title {
    font-family: "Exo 2", sans-serif;
    font-size: 12px;
    letter-spacing: 1.6px;
    color: var(--ink-soft);
    margin-top: 2px;
  }
</style>
</head>
<body>

  <section class="card card--back" aria-label="Business card back">
    <div class="back__panel"></div>
    <div class="brand">
      <div class="brand__mark"></div>
      <div class="brand__name">Halvorne Building and Construction</div>
    </div>
  </section>

  <section class="card card--front" aria-label="Business card front">
    <div class="contact-panel">
      <p class="contact-panel__address">42 Kestrel Row Road<br>5th building Lane</p>
      <ul class="contact-list">
        <li>
          <svg viewBox="0 0 10 10"><path d="M2 0.5l1.6 2.2-1 1c0.6 1.3 1.5 2.2 2.8 2.8l1-1 2.2 1.6-1 2.2C4.2 9 1 5.8 0.3 1.5z"/></svg>
          012 555 0147
        </li>
        <li>
          <svg viewBox="0 0 10 10"><path d="M2.5 0h5v10h-5zM3.3 1v7h3.4V1z"/></svg>
          012 555 0148
        </li>
        <li>
          <svg viewBox="0 0 10 10"><path d="M1 4h8v5H1zM3 0h4v3H3z"/></svg>
          012 555 0149
        </li>
        <li>
          <svg viewBox="0 0 10 10"><path d="M0 2h10v6H0zM0.8 2.6L5 5.6l4.2-3z" fill-rule="evenodd"/></svg>
          aldo@halvorne.com
        </li>
        <li>
          <svg viewBox="0 0 10 10"><circle cx="5" cy="5" r="4.5"/></svg>
          www.halvorne.com
        </li>
      </ul>
    </div>

    <div class="brand">
      <div class="brand__mark"></div>
      <div class="brand__name">Halvorne Building and Construction</div>
    </div>

    <div class="divider"></div>
    <div class="person">
      <h1 class="person__name">ALDO BRENNER</h1>
      <p class="person__title">GENERAL MANAGER</p>
    </div>
  </section>

</body>
</html>
```